Ember Hollow Candles needs an elegant/eye catching packaging design

I need a packaging design for a medium sized candle. (Medium size package including dimensions is uploaded as file). I am going to launch my business next year. I will have 10 fragrances to choose from and have done my fragrance research and I will be to targeting the 25-35 year old market. The theme for this first range will be luxury/elegant candles. I have named my candles Ember Hollow Candles in admiration of this mystic mountain which is close to where I live in Murwillumbah called Wollumbin (Mount Warning), whose local Aboriginal name translates to 'Ember Hollow'
Everyone refers to the mountain as the 'Ember Hollow'.
Mount Warning is the central volcanic remnant of an ancient shield volcano. Often when you look at it, it has clouds caught around it, is is just stunning, and breathtaking to look at! It can be seen from many points in Murwillumbah, its as if it is always watching you. Mount Warning is the central volcanic remnant of an ancient shield volcano. Lieutenant Henry Falcott saw the mountain from the sea and named it Mount Warning. Mount Warning was formed 23 milllion years ago and is the remnant central plug of the Tweed shelf volcano also know as the 'Tweed Caldera' and is one of the largest and best examples of an erosion caldera in the world. it is also a sacred site to the Aboriginal Bundjalung people and its Aboriginal name is Wollumbin. The mountain is now closed to climbers because it is a sacred site. As I will be doing several ranges of Candles, I want to start with a luxury candle to really pay respect to this mystical and stunning grand icon. I I will leave the design and colour to the designer to use their artistic flare but would like something mystical and elegant and eye catching. I do have two logos that I will be using which I have uploaded but the website needs to be added to one of the logos. The blue clouds around the circle logo are not part of my logo. My website emberhollowcandles.com and I am yet to develop it. Many thanks for helping with this design, and I look forward to receiving your ideas. On the package, I would like my Business Logo and a space to put the fragrance name (I will be getting a different colour box for each scent so they each stand out with their own separate identity. I would like this quote on the side or back of the box 'Every cloud has a silver lining' Thanks so much Maudie :-).

Target Market(s)

25-35 year olds

Industry/Entity Type

To be marketed to all types of shops, boutiques, clothing shops. homewares. To be bought by a consumer for a gift for themselves or a gift for family or friends.

Font styles to use
Script

Colors

Designer to choose colors to be used in the design.

Requirements
Must have
• Eye catching, dreamy, mesmorizing, mystical, eye catching packaging design. As I will be using a different coloured pack for each of my ten scents, need a design that can look good in any colours
Nice to have
• Use your artistic flair

```html
<!DOCTYPE html>
<html lang="en">
<head>
<meta charset="utf-8">
<title>Ember Hollow Candles – Box Panels</title>
<link rel="stylesheet" href="https://fonts.googleapis.com/css2?family=Allura&family=Montserrat:wght@400;500&display=swap">
<style>
  :root {
    --stage: #1d1d1f;
    --navy-deep: #0a1a5c;
    --navy: #0f2a8a;
    --navy-light: #1a3aa8;
    --gold: #d6913a;
    --gold-soft: #e8b65e;
    --bronze: #8a6a4c;
    --silver: #e6e6ee;
    --label: #ffffff;
  }
  * { box-sizing: border-box; margin: 0; padding: 0; }
  html, body {
    width: 1200px;
    height: 930px;
    overflow: hidden;
    background: var(--stage);
  }
  .stage {
    position: relative;
    width: 1200px;
    height: 930px;
  }
  .panel {
    position: absolute;
    top: 123px;
    width: 502px;
    height: 623px;
    overflow: hidden;
  }
  .panel--front { left: 68px; }
  .panel--side { left: 600px; width: 500px; }
  .panel__pattern {
    position: absolute;
    inset: 0;
  }
  .panel--front .panel__pattern {
    background: radial-gradient(circle at 50% 50%, var(--navy) 0%, #1b2f7a 45%, #7a5a3a 100%);
  }
  .panel--side .panel__pattern {
    background: radial-gradient(circle at 50% 50%, var(--navy) 0%, #1b2f7a 45%, var(--bronze) 100%);
  }
  .panel__medallion {
    position: absolute;
    border-radius: 50%;
    background: linear-gradient(90deg, var(--navy-deep) 0%, var(--navy) 55%, var(--navy-light) 100%);
    box-shadow: 0 0 18px rgba(0, 0, 0, 0.45);
  }
  .panel--front .panel__medallion { left: 42px; top: 107px; width: 432px; height: 412px; }
  .panel--side .panel__medallion { left: 33px; top: 95px; width: 444px; height: 444px; }

  .product-name {
    position: absolute;
    left: 0; right: 0;
    top: 255px;
    text-align: center;
    font-family: "Allura", cursive;
    font-size: 72px;
    color: var(--silver);
    line-height: 1;
  }
  .product-rule {
    position: absolute;
    left: 79px;
    width: 361px;
    top: 344px;
    height: 2px;
    background: var(--gold);
  }
  .fragrance-name {
    position: absolute;
    left: 0; right: 0;
    top: 361px;
    text-align: center;
    font-family: "Montserrat", sans-serif;
    font-size: 12px;
    letter-spacing: 9px;
    color: var(--silver);
  }
  .tagline {
    position: absolute;
    left: 0; right: 0;
    top: 464px;
    text-align: center;
    font-family: "Montserrat", sans-serif;
    font-size: 10px;
    letter-spacing: 4px;
    color: var(--silver);
  }

  .brand-seal {
    position: absolute;
    left: 163px;
    top: 161px;
    width: 178px;
    height: 178px;
    border: 3px solid var(--gold-soft);
    border-radius: 50%;
    display: flex;
    align-items: center;
    justify-content: center;
    text-align: center;
  }
  .brand-seal__name {
    font-family: "Allura", cursive;
    font-size: 30px;
    line-height: 1;
    color: var(--gold-soft);
  }
  .quote {
    position: absolute;
    left: 0; right: 0;
    top: 380px;
    text-align: center;
    font-family: "Allura", cursive;
    font-size: 34px;
    color: var(--silver);
  }

  .view-label {
    position: absolute;
    top: 792px;
    font-family: "Montserrat", sans-serif;
    font-size: 38px;
    font-weight: 500;
    color: var(--label);
    width: 200px;
    text-align: center;
  }
  .view-label--front { left: 218px; }
  .view-label--side { left: 748px; }
</style>
</head>
<body>
<main class="stage">
  <section class="panel panel--front">
    <div class="panel__pattern" role="img" aria-label="Hand-drawn pattern of concentric gold cloud swirls on deep blue"></div>
    <div class="panel__medallion"></div>
    <h1 class="product-name">Ember Hollow</h1>
    <div class="product-rule"></div>
    <p class="fragrance-name">EARTH BLEND</p>
    <p class="tagline">HANDMADE SOY CANDLES</p>
  </section>

  <section class="panel panel--side">
    <div class="panel__pattern" role="img" aria-label="Hand-drawn pattern of concentric bronze cloud swirls on deep blue"></div>
    <div class="panel__medallion"></div>
    <div class="brand-seal">
      <span class="brand-seal__name">Ember Hollow<br>Candles</span>
    </div>
    <p class="quote">‘Every cloud has a silver lining’</p>
  </section>

  <p class="view-label view-label--front">front</p>
  <p class="view-label view-label--side">side</p>
</main>
</body>
</html>
```